Business Cards for Tax Preparation Business
KRT Tax Preparation
Business Cards for Tax Preparation Business - Financial Services
Creative Brief
Cutting-Edge
Brian K Holloway
Registered Tax Return Preparer
47 Birchmont Avenue, Suite 318 West Hartford, CT 06107
860-555-0148 x36
brian@krtfiling.example
www.krtfiling.example

```html
<!DOCTYPE html>
<html lang="en">
<head>
<meta charset="utf-8">
<title>KRT Tax Preparation – Stationery Set</title>
<link rel="stylesheet" href="https://fonts.googleapis.com/css2?family=Cinzel:wght@700&family=Open+Sans:wght@400;600&display=swap">
<style>
:root{
  --board:#0a1431;
  --paper:#ffffff;
  --blue:#1d4fae;
  --blue-deep:#0f2e78;
  --blue-light:#3f7fe0;
  --gold:#e3b23c;
  --ink:#1c2a4a;
  --muted:#8a94a8;
}
*{box-sizing:border-box;margin:0;padding:0}
html,body{width:1200px;height:197px;overflow:hidden;background:var(--board)}
body{position:relative;font-family:"Open Sans",Arial,sans-serif;color:var(--ink)}
.piece{position:absolute;overflow:hidden;box-shadow:0 2px 5px rgba(0,0,0,.5)}
.white{background:var(--paper)}
.blue{background:linear-gradient(160deg,var(--blue-light),var(--blue) 45%,var(--blue-deep))}
.wave{position:absolute;left:0;bottom:0;width:100%}
.logo{display:flex;align-items:center;gap:2px}
.logo .mark{width:5px;height:5px;background:var(--gold)}
.logo .name{font-family:"Cinzel",Georgia,serif;font-weight:700;color:var(--blue);line-height:1}
.on-blue .name{color:#fff}
.tag{font-size:3px;letter-spacing:.3px;color:var(--muted);text-transform:uppercase}
.small{font-size:3px;line-height:1.35;color:var(--ink)}
.on-blue .small{color:#dfe8ff}
.line{height:1px;background:#d7dce6;margin:2px 0}
.center{display:flex;flex-direction:column;align-items:center;justify-content:center}
</style>
</head>
<body>

<!-- business card back & front -->
<div class="piece blue center on-blue" style="left:5px;top:85px;width:62px;height:36px">
  <div class="logo"><span class="mark"></span><span class="name" style="font-size:9px">KRT</span></div>
</div>
<div class="piece white" style="left:5px;top:130px;width:62px;height:36px;padding:4px">
  <div class="logo"><span class="mark"></span><span class="name" style="font-size:6px">KRT</span></div>
  <div class="small" style="margin-top:3px">Brian K Holloway<br>860-555-0148 x36</div>
  <svg class="wave" viewBox="0 0 62 8" height="8" preserveAspectRatio="none"><path d="M0 5 Q31 0 62 4 V8 H0Z" fill="var(--blue)"/></svg>
</div>

<!-- letterheads -->
<div class="piece white letterhead" style="left:78px;top:6px;width:60px;height:82px;padding:5px">
  <div class="logo"><span class="mark"></span><span class="name" style="font-size:7px">KRT</span></div>
  <div class="tag">Tax Preparation</div>
  <div class="small" style="margin-top:6px">Dear valued client,</div>
  <div class="line"></div><div class="line"></div><div class="line"></div><div class="line"></div><div class="line" style="width:60%"></div>
  <div class="small">Sincerely,</div>
  <svg class="wave" viewBox="0 0 60 12" height="12" preserveAspectRatio="none"><path d="M0 8 Q30 0 60 6 V12 H0Z" fill="var(--blue)"/></svg>
</div>
<div class="piece white letterhead" style="left:145px;top:6px;width:60px;height:82px;padding:5px">
  <div class="logo"><span class="mark"></span><span class="name" style="font-size:7px">KRT</span></div>
  <div class="tag">Tax Preparation</div>
  <div class="line" style="margin-top:10px"></div><div class="line"></div><div class="line"></div><div class="line"></div><div class="line" style="width:50%"></div>
  <svg class="wave" viewBox="0 0 60 12" height="12" preserveAspectRatio="none"><path d="M0 8 Q30 0 60 6 V12 H0Z" fill="var(--blue)"/></svg>
</div>
<div class="piece white letterhead" style="left:78px;top:100px;width:60px;height:82px;padding:5px">
  <div class="logo"><span class="mark"></span><span class="name" style="font-size:7px">KRT</span></div>
  <div class="line" style="margin-top:12px"></div><div class="line"></div><div class="line"></div><div class="line" style="width:70%"></div>
  <svg class="wave" viewBox="0 0 60 12" height="12" preserveAspectRatio="none"><path d="M0 8 Q30 0 60 6 V12 H0Z" fill="var(--blue)"/></svg>
</div>
<div class="piece white letterhead" style="left:145px;top:100px;width:60px;height:82px;padding:5px">
  <div class="logo"><span class="mark"></span><span class="name" style="font-size:7px">KRT</span></div>
  <div class="line" style="margin-top:12px"></div><div class="line"></div><div class="line"></div><div class="line" style="width:70%"></div>
  <svg class="wave" viewBox="0 0 60 12" height="12" preserveAspectRatio="none"><path d="M0 8 Q30 0 60 6 V12 H0Z" fill="var(--blue)"/></svg>
</div>

<!-- business cards -->
<div class="piece white" style="left:218px;top:42px;width:62px;height:36px;padding:4px">
  <div class="logo"><span class="mark"></span><span class="name" style="font-size:6px">KRT</span></div>
  <div class="small" style="margin-top:2px">Brian K Holloway<br>Registered Tax Return Preparer<br>brian@krtfiling.example</div>
  <svg class="wave" viewBox="0 0 62 6" height="6" preserveAspectRatio="none"><path d="M0 4 Q31 0 62 3 V6 H0Z" fill="var(--blue)"/></svg>
</div>
<div class="piece blue center on-blue" style="left:218px;top:84px;width:62px;height:36px">
  <div class="logo"><span class="mark"></span><span class="name" style="font-size:9px">KRT</span></div>
</div>
<div class="piece white" style="left:290px;top:42px;width:62px;height:36px;padding:4px">
  <div class="logo"><span class="mark"></span><span class="name" style="font-size:6px">KRT</span></div>
  <div class="small" style="margin-top:2px">47 Birchmont Avenue, Suite 318<br>West Hartford, CT 06107<br>www.krtfiling.example</div>
</div>
<div class="piece blue center on-blue" style="left:290px;top:84px;width:62px;height:36px">
  <div class="small">www.krtfiling.example</div>
</div>

<!-- DL envelopes -->
<div class="piece white" style="left:218px;top:128px;width:134px;height:28px;padding:3px">
  <div class="logo"><span class="mark"></span><span class="name" style="font-size:6px">KRT</span></div>
  <div class="small">47 Birchmont Avenue, Suite 318 West Hartford, CT 06107</div>
  <svg class="wave" viewBox="0 0 134 6" height="6" preserveAspectRatio="none"><path d="M0 4 Q67 0 134 3 V6 H0Z" fill="var(--blue)"/></svg>
</div>
<div class="piece blue" style="left:218px;top:162px;width:134px;height:28px"></div>

<!-- CD sleeve / square pieces -->
<div class="piece white center" style="left:430px;top:92px;width:120px;height:95px">
  <div class="logo"><span class="mark" style="width:10px;height:10px"></span><span class="name" style="font-size:22px">KRT</span></div>
  <div class="tag" style="font-size:5px;margin-top:3px">Tax Preparation</div>
  <svg class="wave" viewBox="0 0 120 14" height="14" preserveAspectRatio="none"><path d="M0 10 Q60 0 120 8 V14 H0Z" fill="var(--blue)"/></svg>
</div>
<div class="piece blue center on-blue" style="left:560px;top:92px;width:120px;height:95px">
  <div class="small" style="font-size:5px">www.krtfiling.example</div>
</div>

<!-- envelopes -->
<div class="piece white" style="left:700px;top:55px;width:100px;height:55px">
  <svg viewBox="0 0 100 55" width="100" height="55"><path d="M0 0 H100 V18 L50 34 L0 18Z" fill="var(--blue)"/><path d="M0 18 L50 34 L100 18" fill="none" stroke="var(--gold)" stroke-width="1"/></svg>
</div>
<div class="piece white" style="left:700px;top:120px;width:100px;height:55px;padding:5px">
  <div class="logo"><span class="mark"></span><span class="name" style="font-size:8px">KRT</span></div>
  <svg class="wave" viewBox="0 0 100 10" height="10" preserveAspectRatio="none"><path d="M0 7 Q50 0 100 5 V10 H0Z" fill="var(--blue)"/></svg>
</div>

<!-- presentation folder -->
<div class="piece white" style="left:812px;top:25px;width:50px;height:160px">
  <svg class="wave" viewBox="0 0 50 20" height="20" preserveAspectRatio="none"><path d="M0 14 Q25 4 50 10 V20 H0Z" fill="var(--blue)"/></svg>
</div>
<div class="piece blue" style="left:868px;top:15px;width:92px;height:170px;background:linear-gradient(170deg,var(--blue),var(--blue-deep))"></div>
<div class="piece white center" style="left:962px;top:15px;width:106px;height:170px">
  <div class="logo"><span class="mark" style="width:8px;height:8px"></span><span class="name" style="font-size:18px">KRT</span></div>
  <div class="tag" style="font-size:4px;margin-top:2px">Tax Preparation</div>
  <svg class="wave" viewBox="0 0 106 18" height="18" preserveAspectRatio="none"><path d="M0 12 Q53 0 106 9 V18 H0Z" fill="var(--blue)"/></svg>
</div>
<div class="piece blue center on-blue" style="left:1070px;top:15px;width:125px;height:170px">
  <div class="logo"><span class="mark" style="width:8px;height:8px"></span><span class="name" style="font-size:18px">KRT</span></div>
  <div class="small" style="font-size:4px;margin-top:4px">860-555-0148 x36</div>
</div>

</body>
</html>
```